Brenwick Homes Realty is seeking to have his informational, lead capture and Internet presence website

white and blue would be prevailed colors with scenarios of Los Angeles icons: Hollywood sign, Santa Monica pier and other beaches with palm trees. It should include information For Buyers, as well as For Sellers; common terminology in the process of purchase and selling houses and basic steps in the process of purchasing and/or selling a house.
Scroll down type of website is prefer, but tabs would be acceptable. Tabs:
About Us. For Buyers. For Sellers, Contact Us.
Links to: Terminology; process of purchase; process of selling.
Updates

Target Market(s)

Mainly focus on BUYERS.

Industry/Entity Type

California Real Estate

Coding

Coded - Design and coding required

Number of Pages Required

3 page

Colors
0054AA
0677BA
7BADD7
CADEEF
E8F1F8

Requirements
Must have
• a slogan under Brenwick Homes Realty: "Southern California Specialists Since 2004". Houses pictures must be Craftman, Country, or Ranch, but no
Nice to have
• On the first page, ABOUT US should be as a map of where to find what visitor needs: For Buyers ( description and link to2nd Page) including at the end description of the process. On 1st page also services offered For Sellers (description of what we do, -3rd page- and at the bottom, process of purchasing). Pages 2 and 3 might need a link to Terminology that will describe used terms. I see my website having at the bottom of every page with my CONTACT US information as well as invitation to send visitor's info to get personalize service. ALSO need as a legal disclaimer licenses numbers and Regulator. (To be provided to winner)
Should not have
• Listings

```html
<!DOCTYPE html>
<html lang="en">
<head>
<meta charset="utf-8">
<title>Brenwick Homes Realty – Home</title>
<link href="https://fonts.googleapis.com/css2?family=Poppins:wght@300;400;500;600;700&display=swap" rel="stylesheet">
<style>
:root{
  --blue:#2f6fec;
  --blue-dark:#0054aa;
  --blue-mid:#0677ba;
  --blue-soft:#7badd7;
  --blue-pale:#cadeef;
  --blue-wash:#e8f1f8;
  --board:#e4eefb;
  --ink:#1c2230;
  --muted:#8a93a3;
  --line:#e6eaf1;
  --white:#ffffff;
  --band:#f3f5f8;
  --foot-dark:#1c2230;
}
*{box-sizing:border-box;margin:0;padding:0}
html,body{width:1200px;height:4399px;overflow:hidden}
body{background:var(--board);font-family:"Poppins",sans-serif;color:var(--ink);position:relative}
.a{position:absolute}
.img{position:absolute;border-radius:6px;background:linear-gradient(135deg,#9fb3c8,#5d7189)}
.img.warm{background:linear-gradient(135deg,#c9b49a,#6f5a45)}
.img.sky{background:linear-gradient(160deg,#b9d3ee,#6a8db5)}
.img.pool{background:linear-gradient(160deg,#c6dbef,#3f7fc0)}
.img.green{background:linear-gradient(160deg,#bcd2e8,#5f8a63)}
.img.person{background:linear-gradient(160deg,#d6dce4,#7e8794)}
.dot{position:absolute;border-radius:50%;background:radial-gradient(circle at 35% 35%,#c9d6ff,#7f98f2)}

/* ---------- Desktop ---------- */
.desk{position:absolute;left:24px;top:26px;width:717px;height:4232px;background:var(--white);overflow:hidden}
.topbar{position:absolute;left:0;top:0;width:100%;height:20px;background:var(--blue);color:#fff;font-size:5.5px;display:flex;align-items:center;justify-content:space-between;padding:0 10px}
.topbar .contacts{display:flex;gap:12px}
.nav{position:absolute;top:20px;left:0;width:100%;height:40px;display:flex;align-items:center;padding:0 52px;font-size:7px}
.nav .links{display:flex;gap:12px;align-items:center}
.nav .links .on{background:#e9effd;border-radius:10px;padding:3px 8px}
.logo{display:flex;align-items:center;gap:5px;font-weight:600;font-size:8px}
.logo i{width:20px;height:20px;border-radius:50%;background:var(--blue);display:block;flex:none}
.logo small{display:block;font-size:4.5px;font-weight:400;color:var(--muted);line-height:1.2}
.nav .logo{position:absolute;left:314px;line-height:1.15}
.nav .right{position:absolute;right:52px;display:flex;gap:8px;align-items:center}
.btn{background:var(--blue);color:#fff;border-radius:12px;font-size:6.5px;padding:5px 10px;display:inline-flex;gap:4px;align-items:center}
.hero-bg{position:absolute;left:0;top:60px;width:717px;height:330px;background:linear-gradient(180deg,#dfe5ee,#f4f6f9 80%,#fff)}
.hero-round{position:absolute;left:330px;top:-180px;width:400px;height:560px;border-radius:0 0 200px 200px;background:linear-gradient(170deg,#aeb9cc,#7f90b3);opacity:.75}
.label{font-size:7px;letter-spacing:2px;color:var(--blue);text-transform:uppercase;font-weight:500}
.h1{font-size:28px;font-weight:600;line-height:1.1;color:var(--ink)}
.h2{font-size:18px;font-weight:600;line-height:1.25}
.p{font-size:6.5px;color:var(--muted);line-height:1.6}
.card{position:absolute;background:#fff;border-radius:10px;box-shadow:0 6px 22px rgba(30,60,120,.12)}
.field{height:22px;border-radius:11px;background:#f2f4f8;font-size:5.5px;color:#a3abb8;display:flex;align-items:center;justify-content:space-between;padding:0 10px;margin-bottom:14px}
.tabs{display:flex;justify-content:space-around;font-size:6.5px;border-bottom:1px solid var(--line);padding:8px 0}
.tabs .on{color:var(--blue);border-bottom:2px solid var(--blue);padding-bottom:6px;margin-bottom:-9px}
.pill{position:absolute;background:#fff;border-radius:20px;box-shadow:0 6px 18px rgba(30,60,120,.12);display:flex;align-items:center;gap:6px;padding:0 12px;font-size:7px;height:40px}
.avatars{display:flex}
.avatars b{width:12px;height:12px;border-radius:50%;background:#8d96a6;border:1.5px solid #fff;margin-left:-4px}
.brands{position:absolute;top:594px;left:80px;width:560px;display:flex;justify-content:space-between;align-items:center;color:#7a808a;font-weight:600}
.feat{position:absolute;left:80px;width:200px;height:62px;background:#fff;border-radius:8px;box-shadow:0 6px 20px rgba(30,60,120,.1);padding:10px 12px 0 46px}
.feat svg{position:absolute;left:12px;top:18px}
.feat h4{font-size:7.5px;color:var(--blue);font-weight:500;margin-bottom:3px}
.seg{position:absolute;display:flex;gap:8px}
.seg span{font-size:6px;border:1px solid var(--blue);color:var(--blue);border-radius:10px;padding:4px 12px}
.seg .on{background:var(--blue);color:#fff}
.step{position:absolute;width:128px}
.step .img{position:relative;height:120px;display:block}
.num{position:absolute;left:10px;bottom:10px;width:20px;height:20px;border-radius:50%;background:#fff;color:var(--blue);font-size:8px;font-weight:600;display:flex;align-items:center;justify-content:center}
.step h4{font-size:8.5px;font-weight:600;margin-top:10px}
.step .p{margin-top:4px}
.step .more{font-size:6px;color:var(--blue);margin-top:6px;display:block}
.links-row{position:absolute;left:80px;top:1432px;width:556px;height:44px;border-radius:8px;background:var(--blue-wash);display:flex;align-items:center;justify-content:space-around;font-size:7px;color:var(--blue-dark);font-weight:500}
.band{position:absolute;left:0;width:717px;background:linear-gradient(180deg,#eef1f5,#f5f7fa)}
.svc{position:absolute;width:170px;height:172px;background:#fff;border-radius:8px;text-align:center;padding-top:30px;box-shadow:0 4px 16px rgba(30,60,120,.06)}
.svc .ic{width:34px;height:34px;border-radius:50%;background:var(--blue);margin:0 auto 14px;display:flex;align-items:center;justify-content:center}
.svc h4{font-size:7.5px;font-weight:500;margin-bottom:5px}
.svc .p{padding:0 28px}
.hood{position:absolute;border-radius:8px;overflow:hidden}
.hood .n{position:absolute;left:14px;bottom:20px;font-size:22px;font-weight:500;color:#fff}
.hood .c{position:absolute;left:14px;bottom:9px;font-size:6px;color:#fff}
.member{position:absolute;width:100px;text-align:center}
.member .img{position:relative;height:138px;display:block;border-radius:8px}
.member h4{font-size:9.5px;font-weight:600;margin-top:12px;white-space:nowrap}
.member span{font-size:6px;color:var(--blue)}
.blogband{position:absolute;left:0;top:2924px;width:717px;height:444px;background:linear-gradient(135deg,#3a7cf0,#1f5fd8)}
.blog{position:absolute;width:170px;color:#fff}
.blog .img{position:relative;height:165px;display:block}
.date{position:absolute;left:26px;top:0;background:#fff;color:var(--ink);font-size:6px;text-align:center;padding:3px 4px;border-radius:0 0 3px 3px;line-height:1.1}
.blog h4{font-size:11px;font-weight:500;line-height:1.35;margin-top:12px}
.blog .p{color:#b9ceff;margin-top:6px}
.arrow{position:absolute;width:20px;height:20px;border-radius:50%;background:#fff;display:flex;align-items:center;justify-content:center}
.ring{width:20px;height:20px;border-radius:50%;border:1px solid var(--blue);display:inline-flex;align-items:center;justify-content:center}
.agent{position:absolute;left:60px;top:3784px;width:598px;height:130px;border-radius:12px;background:linear-gradient(120deg,#2d6de8,#5c96f5);overflow:hidden}
.footer{position:absolute;left:0;top:4000px;width:717px;height:214px;background:#f6f7f9}
.fcol{position:absolute;top:46px;font-size:6px;color:#444;line-height:2}
.fcol h5{font-size:7.5px;font-weight:500;color:var(--ink);margin-bottom:6px}
.bottombar{position:absolute;left:0;top:4214px;width:717px;height:18px;background:var(--foot-dark);color:#aab;font-size:5px;display:flex;align-items:center;padding:0 12px}

/* ---------- Mobile ---------- */
.mob{position:absolute;left:777px;top:26px;width:163px;height:4359px;background:#fff;overflow:hidden}
.mob .p{font-size:3.6px}
.mob .label{font-size:4px;letter-spacing:1px}
.mh{font-size:9px;font-weight:600;line-height:1.2}
.mob .img{border-radius:4px}
.mtxt{position:absolute;font-size:4.5px}
.mcard{position:absolute;background:#fff;border-radius:6px;box-shadow:0 3px 10px rgba(30,60,120,.12)}
.mfield{height:10px;border-radius:5px;background:#f2f4f8;margin:0 8px 6px;font-size:3px;color:#aab;padding-left:5px;line-height:10px}
.mbtn{background:var(--blue);color:#fff;border-radius:6px;font-size:3.8px;text-align:center;height:11px;line-height:11px}

/* ---------- Phone ---------- */
.phone{position:absolute;left:987px;top:28px;width:176px;height:362px;background:#fff;border-radius:18px;overflow:hidden;box-shadow:0 4px 14px rgba(30,60,120,.12)}
</style>
</head>
<body>

<!-- ================= DESKTOP ================= -->
<main class="desk">
  <div class="topbar">
    <span>Brenwick, 42 Palm Ave, Glendale</span>
    <span class="contacts"><span>+1 310-555-0147</span><span>hello@brenwickhomes.com</span></span>
  </div>
  <div class="hero-bg" role="img" aria-label="Faded Los Angeles skyline with palm trees behind the hero">
    <div class="hero-round"></div>
  </div>
  <nav class="nav">
    <div class="links"><span class="on">Home</span><span>About Us</span><span>For Buyers</span><span>For Sellers</span><span>Contact Us</span></div>
    <div class="logo"><i></i><span>Brenwick Homes Realty<small>Southern California Specialists Since 2004</small></span></div>
    <div class="right"><span>Login/Register</span><span class="btn">+ Get Started</span></div>
  </nav>

  <div class="a label" style="left:80px;top:104px">Real Estate</div>
  <h1 class="a h1" style="left:80px;top:118px;width:300px">Find a perfect<br>home you love..!</h1>
  <p class="a p" style="left:80px;top:192px;width:270px">Etiam eget elementum elit. Aenean dignissim dapibus vestibulum. Integer a dolor eu sapien sodales vulputate ac in purus.</p>
  <div class="img warm" style="left:80px;top:234px;width:281px;height:175px" role="img" aria-label="Bright bedroom interior with large windows"></div>
  <div class="dot" style="left:336px;top:218px;width:26px;height:26px"></div>

  <div class="card" style="left:428px;top:121px;width:208px;height:290px">
    <div class="tabs"><span class="on">For Sale</span><span>For Buy</span></div>
    <div style="padding:20px 20px 0">
      <div class="field">Los Angeles, Pasadena etc</div>
      <div class="field">Select Property Type <span>⌄</span></div>
      <div class="field">Select Rooms <span>⌄</span></div>
      <div style="font-size:5px;color:var(--blue);margin:-6px 0 26px">☰ Advance Search</div>
      <div class="btn" style="display:flex;justify-content:center;padding:7px">Search</div>
    </div>
  </div>

  <div class="pill" style="left:180px;top:449px;width:150px"><span class="avatars"><b></b><b></b><b></b><b></b><b></b></span><span>72k+ Happy<br>Customers</span></div>
  <div class="pill" style="left:395px;top:449px;width:142px"><span class="img" style="position:relative;width:22px;height:22px;border-radius:50%"></span><span>20+ Years<br>in Southern California</span></div>

  <div class="dot" style="left:98px;top:522px;width:50px;height:50px"></div>
  <div class="a p" style="left:0;width:717px;text-align:center;top:552px">Trusted by 100+ Companies across the globe!</div>
  <div class="brands">
    <span style="font-size:15px;font-weight:500">Norvale</span>
    <span style="font-size:13px">Cartwell</span>
    <span style="font-size:13px;font-weight:500">Lumetra</span>
    <span style="font-size:10px">● Sonnet</span>
    <span style="font-size:9px;letter-spacing:1px">KORVIS</span>
    <span style="font-size:11px;letter-spacing:1px">REELBOX</span>
  </div>

  <!-- About -->
  <div class="a label" style="left:80px;top:718px">Who are we</div>
  <h2 class="a h2" style="left:80px;top:738px;width:260px">Assisting individuals in locating the appropriate real estate.</h2>
  <p class="a p" style="left:80px;top:820px;width:240px">Donec porttitor euismod dignissim. Nullam a lacinia ipsum, nec dignissim purus. Nulla convallis ipsum molestie nibh malesuada, ac malesuada leo volutpat.</p>
  <div class="feat" style="top:858px"><svg width="22" height="22" viewBox="0 0 24 24" fill="none" stroke="#2f6fec" stroke-width="1.6"><path d="M3 11l9-7 9 7v9H3z"/></svg><h4>For Buyers</h4><p class="p">Guidance from search to keys, step by step.</p></div>
  <div class="feat" style="top:938px"><svg width="22" height="22" viewBox="0 0 24 24" fill="none" stroke="#2f6fec" stroke-width="1.6"><circle cx="12" cy="12" r="10"/><circle cx="12" cy="10" r="3"/><path d="M6 19c2-3 10-3 12 0"/></svg><h4>For Sellers</h4><p class="p">Pricing, staging and marketing your home.</p></div>
  <svg class="a" style="left:440px;top:700px" width="80" height="80" viewBox="0 0 80 80"><defs><path id="arc" d="M40 40 m-30 0 a30 30 0 1 1 60 0"/></defs><text font-size="6.5" fill="#2f6fec" letter-spacing="2" font-family="Poppins,sans-serif"><textPath href="#arc">Since 2004 • Real Estate</textPath></text></svg>
  <div class="img pool" style="left:350px;top:770px;width:138px;height:250px" role="img" aria-label="Craftsman house with front porch"></div>
  <div class="img warm" style="left:500px;top:750px;width:138px;height:140px" role="img" aria-label="Cozy bedroom interior"></div>
  <div class="img warm" style="left:500px;top:900px;width:138px;height:94px" role="img" aria-label="Living room with sofa"></div>
  <div class="dot" style="left:540px;top:982px;width:24px;height:24px"></div>

  <!-- Buyers & Sellers process -->
  <div class="a label" style="left:80px;top:1120px">Your path home</div>
  <h2 class="a h2" style="left:80px;top:1136px">How Buying Works</h2>
  <p class="a p" style="left:80px;top:1166px;width:250px">Four clear steps from first look to closing day, with an agent beside you the whole way.</p>
  <div class="seg" style="left:476px;top:1150px"><span class="on">Buyers</span><span>Sellers</span><span>Terms</span></div>
  <div class="step" style="left:80px;top:1216px"><div class="img sky" role="img" aria-label="Craftsman home exterior"><span class="num">1</span></div><h4>Get Pre-Approved</h4><p class="p">Know your budget before you tour homes with a lender letter.</p><span class="more">Learn more →</span></div>
  <div class="step" style="left:224px;top:1216px"><div class="img warm" role="img" aria-label="Ranch style house"><span class="num">2</span></div><h4>Tour &amp; Choose</h4><p class="p">We shortlist homes that fit your needs, area and price range.</p><span class="more">Learn more →</span></div>
  <div class="step" style="left:368px;top:1216px"><div class="img green" role="img" aria-label="Country home with garden"><span class="num">3</span></div><h4>Offer &amp; Escrow</h4><p class="p">We write a strong offer, then guide inspections and appraisal.</p><span class="more">Learn more →</span></div>
  <div class="step" style="left:512px;top:1216px"><div class="img pool" role="img" aria-label="Palm-lined street at sunset"><span class="num">4</span></div><h4>Close &amp; Move In</h4><p class="p">Sign final papers, receive your keys and settle into home.</p><span class="more">Learn more →</span></div>
  <div class="links-row"><span>For Buyers →</span><span>For Sellers →</span><span>Terminology →</span><span>Contact Us →</span></div>

  <!-- Services -->
  <div class="band" style="top:1564px;height:370px" role="img" aria-label="Faded city skyline background"></div>
  <div class="a label" style="left:0;width:717px;text-align:center;top:1612px;color:#444">Our Services</div>
  <h2 class="a h2" style="left:0;width:717px;text-align:center;top:1630px">Donec porttitor euismod dignissim</h2>
  <div class="svc" style="left:80px;top:1685px"><div class="ic"><svg width="14" height="14" viewBox="0 0 24 24" fill="none" stroke="#fff" stroke-width="2.2"><circle cx="10" cy="10" r="6"/><path d="M15 15l5 5"/></svg></div><h4>Buy a New Home</h4><p class="p">Donec porttitor euismod dignissim. Nullam a lacinia ipsum, nec dignissim purus.</p></div>
  <div class="svc" style="left:274px;top:1685px"><div class="ic"><svg width="14" height="14" viewBox="0 0 24 24" fill="none" stroke="#fff" stroke-width="2.2"><path d="M3 11l9-7 9 7v9H3z"/></svg></div><h4>Sell a House</h4><p class="p">Donec porttitor euismod dignissim. Nullam a lacinia ipsum, nec dignissim purus.</p></div>
  <div class="svc" style="left:468px;top:1685px"><div class="ic"><svg width="14" height="14" viewBox="0 0 24 24" fill="none" stroke="#fff" stroke-width="2.2"><path d="M3 6v13M3 14h18v5M8 11h13v3"/></svg></div><h4>Rent a House</h4><p class="p">Donec porttitor euismod dignissim. Nullam a lacinia ipsum, nec dignissim purus.</p></div>

  <!-- Neighborhood -->
  <div class="dot" style="left:330px;top:1970px;width:24px;height:24px"></div>
  <div class="a label" style="left:80px;top:2036px">Areas across the town</div>
  <h2 class="a h2" style="left:80px;top:2054px">Neighborhood Properties</h2>
  <div class="hood img" style="left:80px;top:2116px;width:150px;height:160px" role="img" aria-label="Los Angeles skyline"><span class="n">216</span><span class="c">Los Angeles, CA</span></div>
  <div class="hood img" style="left:254px;top:2116px;width:150px;height:160px" role="img" aria-label="Pasadena streets"><span class="n">141</span><span class="c">Pasadena, CA</span></div>
  <div class="hood img warm" style="left:428px;top:2116px;width:208px;height:160px" role="img" aria-label="San Diego house"><span class="n">212</span><span class="c">San Diego, CA</span></div>
  <div class="hood img green" style="left:80px;top:2296px;width:206px;height:160px" role="img" aria-label="Santa Monica beach"><span class="n">183</span><span class="c">Santa Monica, CA</span></div>
  <div class="hood img warm" style="left:310px;top:2296px;width:326px;height:160px" role="img" aria-label="Glendale house"><span class="n">112</span><span class="c">Glendale, CA</span></div>
  <div class="dot" style="left:556px;top:2492px;width:50px;height:50px"></div>

  <!-- Team -->
  <div class="a label" style="left:0;width:717px;text-align:center;top:2562px">Introduce yourself to</div>
  <h2 class="a h2" style="left:0;width:717px;text-align:center;top:2580px">Our Team of Experts</h2>
  <div class="member" style="left:106px;top:2654px"><div class="img person" role="img" aria-label="Portrait of team member"></div><h4>Darren K</h4><span>CEO &amp; Founder</span></div>
  <div class="member" style="left:240px;top:2654px"><div class="img person" role="img" aria-label="Portrait of team member"></div><h4>Nina R. Castell</h4><span>Real Estate Developer</span></div>
  <div class="member" style="left:374px;top:2654px"><div class="img person" role="img" aria-label="Portrait of team member"></div><h4>Owen T. Reyes</h4><span>Listing Agent</span></div>
  <div class="member" style="left:508px;top:2654px"><div class="img person" role="img" aria-label="Portrait of team member"></div><h4>Clara M. Dunn</h4><span>Buyer's Agent</span></div>

  <!-- Blogs -->
  <div class="blogband"></div>
  <div class="a label" style="left:0;width:717px;text-align:center;top:2984px;color:#dbe6ff">What's trending</div>
  <h2 class="a h2" style="left:0;width:717px;text-align:center;top:3000px;color:#fff">Latest Blogs &amp; Posts</h2>
  <div class="blog" style="left:80px;top:3050px"><div class="img warm" role="img" aria-label="Hands signing papers at a desk"><span class="date">28<br>Mon</span></div><h4>Top 10 Home Buying Mistakes to Avoid</h4><p class="p">Etiam eget elementum elit. Aenean dignissim dapibus vestibulum.</p></div>
  <div class="blog" style="left:274px;top:3050px"><div class="img" role="img" aria-label="Keys and documents on a table"><span class="date">08<br>Tue</span></div><h4>How to Stage Your Home for a Quick Sale</h4><p class="p">Nullam odio lacus, dictum quis pretium congue, vehicula venenatis nunc.</p></div>
  <div class="blog" style="left:468px;top:3050px"><div class="img sky" role="img" aria-label="Agent meeting clients in an office"><span class="date">26<br>Wed</span></div><h4>5 Tips for First-Time Home Sellers</h4><p class="p">In hac habitasse platea dictumst. Phasellus vel sem et augue maximus.</p></div>
  <div class="arrow" style="left:231px;top:3300px"><svg width="9" height="9" viewBox="0 0 10 10" fill="none" stroke="#2f6fec" stroke-width="1.4"><path d="M1 5h8M6 2l3 3-3 3"/></svg></div>
  <div class="arrow" style="left:425px;top:3300px"><svg width="9" height="9" viewBox="0 0 10 10" fill="none" stroke="#2f6fec" stroke-width="1.4"><path d="M1 5h8M6 2l3 3-3 3"/></svg></div>
  <div class="arrow" style="left:619px;top:3300px"><svg width="9" height="9" viewBox="0 0 10 10" fill="none" stroke="#2f6fec" stroke-width="1.4"><path d="M1 5h8M6 2l3 3-3 3"/></svg></div>

  <!-- Testimonials -->
  <div class="a label" style="left:80px;top:3452px">Testimonials</div>
  <h2 class="a h2" style="left:80px;top:3470px;width:200px">Look What Our Customers Say!</h2>
  <p class="a p" style="left:80px;top:3520px;width:190px">Fusce venenatis tellus a felis scelerisque, non pulvinar est pellentesque.</p>
  <div class="a" style="left:80px;top:3556px;display:flex;gap:10px"><span class="ring"><svg width="8" height="8" viewBox="0 0 10 10" fill="none" stroke="#2f6fec" stroke-width="1.4"><path d="M9 5H1M4 2L1 5l3 3"/></svg></span><span class="ring"><svg width="8" height="8" viewBox="0 0 10 10" fill="none" stroke="#2f6fec" stroke-width="1.4"><path d="M1 5h8M6 2l3 3-3 3"/></svg></span></div>
  <div class="dot" style="left:366px;top:3474px;width:24px;height:24px"></div>
  <div class="card" style="left:400px;top:3490px;width:240px;height:196px;padding:26px 28px">
    <div style="font-size:30px;color:#f2c94c;line-height:.8;font-weight:700">“</div>
    <p style="font-size:8.5px;line-height:1.5;margin-top:4px">I highly recommend Nina R. Castell. She was attentive to our needs and worked tirelessly to find us the perfect home. We couldn't be happier with our new place!</p>
    <div style="display:flex;align-items:center;gap:6px;margin-top:16px;font-size:7px"><span class="img person" style="position:relative;width:18px;height:18px;border-radius:50%"></span>Helen P. Moss<span style="margin-left:auto;color:#f2b01e;font-size:7px">★★★★★</span></div>
  </div>
  <div class="a" style="left:660px;top:3540px;width:2px;height:22px;background:#333"></div>
  <div class="a" style="left:660px;top:3570px;width:2px;height:22px;background:#ccd"></div>

  <!-- Become an agent -->
  <div class="agent">
    <div class="img person" style="left:40px;top:-6px;width:100px;height:136px;border-radius:0;opacity:.85" role="img" aria-label="Smiling agent in a suit"></div>
    <div class="a" style="left:190px;top:40px;color:#fff;font-size:17px;font-weight:600">Become a Agent.</div>
    <div class="a" style="left:190px;top:68px;color:#dbe6ff;font-size:6px;width:130px;line-height:1.5">Fusce venenatis tellus a felis scelerisque venenatis tellus a felis scelerisque.</div>
    <div class="a" style="left:404px;top:52px;background:#fff;color:var(--blue);font-size:6px;border-radius:10px;padding:5px 14px">Register Now</div>
  </div>

  <!-- Footer -->
  <footer class="footer" role="contentinfo">
    <div class="fcol" style="left:80px"><div class="logo" style="margin-bottom:10px;line-height:1.2"><i></i><span>Brenwick Homes Realty<small>Southern California Specialists Since 2004</small></span></div>1840 Alder Lane<br>Pasadena, CA 91101<br><br>☏ +1 310-555-0147<br>✉ hello@brenwickhomes.com</div>
    <div class="fcol" style="left:238px"><h5>Quick Links</h5>Home<br>About Us<br>For Buyers<br>For Sellers<br>Terminology<br>Contact Us</div>
    <div class="fcol" style="left:360px"><h5>Discovery</h5>Los Angeles<br>Pasadena<br>Santa Monica<br>Glendale<br>San Diego</div>
    <div class="fcol" style="left:464px;width:170px"><h5>Subscribe to our<br>Newsletter!</h5>
      <div style="background:#fff;border-radius:12px;height:26px;display:flex;align-items:center;justify-content:space-between;padding:0 4px 0 10px;color:#aab;font-size:5.5px">Email Address<span style="width:20px;height:20px;border-radius:50%;background:var(--blue);display:inline-block"></span></div>
      <h5 style="margin-top:8px">Follow Us on</h5>
      <div style="display:flex;gap:6px"><span style="width:9px;height:9px;border-radius:50%;background:var(--blue)"></span><span style="width:9px;height:9px;border-radius:50%;background:var(--blue)"></span><span style="width:9px;height:9px;border-radius:50%;background:var(--blue)"></span></div>
    </div>
  </footer>
  <div class="bottombar"><span>© Brenwick Homes Realty - All rights reserved</span><span style="margin-left:auto;display:flex;gap:16px"><span>Terms and Conditions</span><span>Privacy Policy</span><span>Disclaimer</span></span></div>
</main>

<!-- ================= MOBILE ================= -->
<main class="mob">
  <div class="a" style="left:12px;top:8px"><div class="logo" style="font-size:4.5px;gap:3px"><i style="width:9px;height:9px"></i>Brenwick Homes Realty</div></div>
  <div class="a" style="right:12px;top:8px;font-size:7px">≡</div>
  <div class="a label" style="left:12px;top:48px">Real Estate</div>
  <div class="a mh" style="left:12px;top:56px;width:140px;font-size:11px">Find a perfect home you love..!</div>
  <p class="a p" style="left:12px;top:84px;width:130px">Etiam eget elementum elit. Aenean dignissim dapibus vestibulum. Integer a dolor eu sapien sodales.</p>
  <div class="img warm" style="left:12px;top:112px;width:139px;height:80px" role="img" aria-label="Bedroom interior"></div>
  <div class="mcard" style="left:12px;top:250px;width:139px;height:120px">
    <div style="display:flex;justify-content:space-around;font-size:4px;padding:6px 0;border-bottom:1px solid var(--line);margin-bottom:8px"><span style="color:var(--blue)">For Sale</span><span>For Rent</span></div>
    <div class="mfield">Los Angeles, Pasadena etc</div><div class="mfield">Select Property Type</div><div class="mfield">Select Rooms</div>
    <div style="font-size:3px;color:var(--blue);margin:0 8px 8px">Advance Search</div>
    <div class="mbtn" style="margin:0 8px">Search</div>
  </div>
  <p class="a p" style="left:0;width:163px;text-align:center;top:462px">Trusted by 100+ Companies<br>across the globe!</p>
  <div class="a" style="left:12px;top:494px;display:flex;gap:12px;font-weight:600;color:#777;font-size:8px"><span>Norvale</span><span>Cartwell</span><span>Lumetra</span></div>
  <div class="mcard" style="left:12px;top:530px;width:139px;height:30px;font-size:4px;display:flex;align-items:center;gap:5px;padding-left:10px"><span class="avatars"><b style="width:8px;height:8px"></b><b style="width:8px;height:8px"></b><b style="width:8px;height:8px"></b><b style="width:8px;height:8px"></b></span>72k+ Happy Customers</div>
  <div class="mcard" style="left:12px;top:580px;width:139px;height:30px;font-size:4px;display:flex;align-items:center;gap:5px;padding-left:10px"><span class="img" style="position:relative;width:14px;height:14px;border-radius:50%"></span>20+ Years in Southern California</div>

  <div class="a label" style="left:12px;top:666px">Who are we</div>
  <div class="a mh" style="left:12px;top:676px;width:140px">Assisting individuals in locating the appropriate real estate.</div>
  <p class="a p" style="left:12px;top:725px;width:135px">Donec porttitor euismod dignissim. Nullam a lacinia ipsum, nec dignissim purus. Nulla convallis ipsum molestie nibh.</p>
  <div class="img pool" style="left:12px;top:790px;width:68px;height:110px" role="img" aria-label="Craftsman house"></div>
  <div class="img warm" style="left:90px;top:790px;width:60px;height:55px" role="img" aria-label="Bedroom"></div>
  <div class="img warm" style="left:90px;top:852px;width:60px;height:40px" role="img" aria-label="Living room"></div>
  <div class="mcard" style="left:12px;top:925px;width:139px;height:34px;padding:7px 0 0 30px"><div style="font-size:4px;color:var(--blue)">For Buyers</div><p class="p">Guidance from search to keys.</p></div>
  <div class="mcard" style="left:12px;top:982px;width:139px;height:34px;padding:7px 0 0 30px"><div style="font-size:4px;color:var(--blue)">For Sellers</div><p class="p">Pricing, staging and marketing.</p></div>

  <div class="a label" style="left:12px;top:1068px">Your path home</div>
  <div class="a mh" style="left:12px;top:1078px">How Buying Works</div>
  <p class="a p" style="left:12px;top:1094px;width:130px">Four clear steps from first look to closing day.</p>
  <div class="a" style="left:12px;top:1130px;display:flex;gap:10px;font-size:3.5px;color:var(--blue)"><span style="background:var(--blue);color:#fff;border-radius:5px;padding:2px 8px">Buyers</span><span style="border:1px solid var(--blue);border-radius:5px;padding:2px 8px">Sellers</span><span style="border:1px solid var(--blue);border-radius:5px;padding:2px 8px">Terms</span></div>
  <div class="img sky" style="left:12px;top:1173px;width:139px;height:90px" role="img" aria-label="Craftsman home"></div>
  <div class="mtxt" style="left:12px;top:1268px;line-height:1.5;width:139px">1. Get Pre-Approved<br><span style="color:#999;font-size:3.5px">Know your budget before you tour homes.</span></div>
  <div class="img warm" style="left:12px;top:1322px;width:139px;height:90px" role="img" aria-label="Ranch style house"></div>
  <div class="mtxt" style="left:12px;top:1417px;line-height:1.5;width:139px">2. Tour &amp; Choose<br><span style="color:#999;font-size:3.5px">We shortlist homes that fit your needs.</span></div>
  <div class="img green" style="left:12px;top:1472px;width:139px;height:90px" role="img" aria-label="Country home"></div>
  <div class="mtxt" style="left:12px;top:1567px;line-height:1.5;width:139px">3. Offer &amp; Escrow<br><span style="color:#999;font-size:3.5px">Strong offer, inspections and appraisal.</span></div>
  <div class="img pool" style="left:12px;top:1622px;width:139px;height:90px" role="img" aria-label="Palm-lined street"></div>
  <div class="mtxt" style="left:12px;top:1717px;line-height:1.5;width:139px">4. Close &amp; Move In<br><span style="color:#999;font-size:3.5px">Sign final papers and receive your keys.</span></div>
  <div class="a" style="left:35px;top:1790px;width:93px;font-size:3.5px;color:var(--blue);border:1px solid var(--blue);border-radius:6px;text-align:center;padding:2px 0">View terminology</div>

  <div class="band" style="top:1830px;width:163px;height:520px" role="img" aria-label="Faded city skyline"></div>
  <div class="a label" style="left:0;width:163px;text-align:center;top:1896px;color:#444">Our Services</div>
  <div class="a mh" style="left:0;width:163px;text-align:center;top:1906px">Donec porttitor<br>euismod dignissim</div>
  <div class="mcard" style="left:16px;top:1960px;width:131px;height:90px;text-align:center;padding-top:18px"><div style="width:16px;height:16px;border-radius:50%;background:var(--blue);margin:0 auto 6px"></div><div style="font-size:4px">Buy a New Home</div><p class="p" style="padding:2px 18px">Donec porttitor euismod dignissim. Nullam a lacinia ipsum.</p></div>
  <div class="mcard" style="left:16px;top:2072px;width:131px;height:90px;text-align:center;padding-top:18px"><div style="width:16px;height:16px;border-radius:50%;background:var(--blue);margin:0 auto 6px"></div><div style="font-size:4px">Sell a House</div><p class="p" style="padding:2px 18px">Donec porttitor euismod dignissim. Nullam a lacinia ipsum.</p></div>
  <div class="mcard" style="left:16px;top:2186px;width:131px;height:100px;text-align:center;padding-top:18px"><div style="width:16px;height:16px;border-radius:50%;background:var(--blue);margin:0 auto 6px"></div><div style="font-size:4px">Rent a House</div><p class="p" style="padding:2px 18px">Donec porttitor euismod dignissim. Nullam a lacinia ipsum.</p></div>

  <div class="a label" style="left:12px;top:2370px">Areas across the town</div>
  <div class="a mh" style="left:12px;top:2380px">Neighborhood<br>Properties</div>
  <div class="img" style="left:12px;top:2416px;width:64px;height:60px" role="img" aria-label="Los Angeles skyline"></div>
  <div class="img" style="left:86px;top:2416px;width:64px;height:60px" role="img" aria-label="Pasadena streets"></div>
  <div class="img warm" style="left:12px;top:2484px;width:64px;height:60px" role="img" aria-label="San Diego house"></div>
  <div class="img green" style="left:86px;top:2484px;width:64px;height:60px" role="img" aria-label="Santa Monica beach"></div>
  <div class="img warm" style="left:12px;top:2552px;width:64px;height:60px" role="img" aria-label="Glendale house"></div>

  <div class="a label" style="left:0;width:163px;text-align:center;top:2660px">Introduce yourself to</div>
  <div class="a mh" style="left:0;width:163px;text-align:center;top:2670px;font-size:8px">Our Team of Experts</div>
  <div class="img person" style="left:20px;top:2698px;width:50px;height:70px" role="img" aria-label="Team member portrait"></div>
  <div class="img person" style="left:92px;top:2698px;width:50px;height:70px" role="img" aria-label="Team member portrait"></div>
  <div class="mtxt" style="left:20px;top:2772px;font-size:3.5px">Darren K</div><div class="mtxt" style="left:92px;top:2772px;font-size:3.5px">Nina R. Castell</div>
  <div class="img person" style="left:20px;top:2806px;width:50px;height:70px" role="img" aria-label="Team member portrait"></div>
  <div class="img person" style="left:92px;top:2806px;width:50px;height:70px" role="img" aria-label="Team member portrait"></div>
  <div class="mtxt" style="left:20px;top:2880px;font-size:3.5px">Owen T. Reyes</div><div class="mtxt" style="left:92px;top:2880px;font-size:3.5px">Clara M. Dunn</div>

  <div class="a" style="left:0;top:2950px;width:163px;height:610px;background:linear-gradient(160deg,#3a7cf0,#1f5fd8)"></div>
  <div class="a label" style="left:0;width:163px;text-align:center;top:2986px;color:#dbe6ff">What's trending</div>
  <div class="a mh" style="left:0;width:163px;text-align:center;top:2996px;color:#fff;font-size:8px">Latest Blogs &amp; Posts</div>
  <div class="img warm" style="left:12px;top:3026px;width:139px;height:80px" role="img" aria-label="Signing papers"></div>
  <div class="mtxt" style="left:12px;top:3112px;color:#fff;width:135px">Top 10 Home Buying Mistakes to Avoid</div>
  <div class="img" style="left:12px;top:3170px;width:139px;height:80px" role="img" aria-label="Keys on a table"></div>
  <div class="mtxt" style="left:12px;top:3256px;color:#fff;width:135px">How to Stage Your Home for a Quick Sale</div>
  <div class="img sky" style="left:12px;top:3316px;width:139px;height:80px" role="img" aria-label="Agent meeting"></div>
  <div class="mtxt" style="left:12px;top:3402px;color:#fff;width:135px">5 Tips for First-Time Home Sellers</div>
  <div class="a" style="left:22px;top:3480px;background:#fff;color:var(--blue);font-size:3.5px;border-radius:6px;padding:2px 10px">View more blogs</div>

  <div class="a label" style="left:12px;top:3604px">Testimonials</div>
  <div class="a mh" style="left:12px;top:3614px;font-size:8px">Look What Our<br>Customers Say!</div>
  <div class="mcard" style="left:12px;top:3680px;width:139px;height:120px;padding:12px 14px"><div style="color:#f2c94c;font-size:16px;line-height:.7">“</div><p style="font-size:4px;line-height:1.5">I highly recommend Nina R. Castell. She was attentive to our needs and worked tirelessly to find us the perfect home.</p><div style="font-size:3.5px;margin-top:8px">Helen P. Moss <span style="color:#f2b01e">★★★★★</span></div></div>

  <div class="a" style="left:12px;top:3830px;width:139px;height:225px;border-radius:8px;background:linear-gradient(160deg,#2d6de8,#5c96f5);overflow:hidden">
    <div class="a" style="left:14px;top:40px;color:#fff;font-size:8px;font-weight:600">Become a Agent.</div>
    <div class="a" style="left:14px;top:54px;color:#dbe6ff;font-size:3.5px;width:100px">Fusce venenatis tellus a felis scelerisque venenatis.</div>
    <div class="a" style="left:14px;top:76px;background:#fff;color:var(--blue);font-size:3.5px;border-radius:5px;padding:2px 8px">Register Now</div>
    <div class="img person" style="left:30px;top:110px;width:80px;height:115px;border-radius:0" role="img" aria-label="Smiling agent"></div>
  </div>

  <div class="a" style="left:0;top:4080px;width:163px;height:279px;background:#f6f7f9;text-align:center;font-size:3.8px;color:#555;line-height:1.8;padding-top:28px">
    <div class="logo" style="justify-content:center;font-size:4.5px"><i style="width:10px;height:10px"></i>Brenwick Homes Realty</div>
    1840 Alder Lane<br>Pasadena, CA 91101<br>+1 310-555-0147<br>hello@brenwickhomes.com<br><br><b style="font-weight:500;color:var(--ink)">Subscribe to our<br>Newsletter!</b>
    <div style="margin:6px 12px;background:#fff;border-radius:6px;height:12px;text-align:left;padding-left:6px;color:#aab">Email Address</div>
    <b style="font-weight:500;color:var(--ink)">Follow Us on</b>
    <div style="display:flex;justify-content:center;gap:6px;margin-top:3px"><span style="width:5px;height:5px;border-radius:50%;background:var(--blue)"></span><span style="width:5px;height:5px;border-radius:50%;background:var(--blue)"></span><span style="width:5px;height:5px;border-radius:50%;background:var(--blue)"></span></div>
  </div>
  <div class="a" style="left:0;top:4349px;width:163px;height:10px;background:var(--foot-dark);color:#aab;font-size:3px;text-align:center;line-height:10px">© Brenwick Homes Realty - All rights reserved</div>
</main>

<!-- ================= PHONE VIEW ================= -->
<main class="phone">
  <div class="a" style="left:12px;top:14px"><div class="logo" style="font-size:5px;gap:3px"><i style="width:11px;height:11px"></i>Brenwick Homes Realty</div></div>
  <div class="a" style="right:12px;top:12px;font-size:8px">≡</div>
  <div class="a" style="left:0;top:36px;width:176px;height:150px;background:linear-gradient(180deg,#dfe5ee,#fff)"></div>
  <div class="a label" style="left:12px;top:46px;font-size:4.5px;letter-spacing:1px">Real Estate</div>
  <div class="a" style="left:12px;top:54px;font-size:12px;font-weight:600;line-height:1.15;width:160px">Find a perfect<br>home you love..!</div>
  <p class="a p" style="left:12px;top:86px;width:140px;font-size:4px">Etiam eget elementum elit. Aenean dignissim dapibus vestibulum. Integer a dolor eu sapien sodales.</p>
  <div class="img warm" style="left:12px;top:112px;width:152px;height:60px" role="img" aria-label="Bedroom interior"></div>
  <div class="mcard" style="left:12px;top:184px;width:152px;height:60px">
    <div style="display:flex;justify-content:space-around;font-size:4.5px;padding:7px 0;border-bottom:1px solid var(--line);margin-bottom:8px"><span style="color:var(--blue)">For Sale</span><span>For Rent</span></div>
    <div class="mfield">Los Angeles, Pasadena etc</div>
  </div>
</main>

</body>
</html>
```